Modern and strong website design for a Dutch crowdsourcing company
.

We are startup company providing crowdsourcing of administrative and customers service tasks for larger companies and other organizations. We offer cost savings and scale-ability combined with higher quality of execution. We will soon enter the market and need a website that has two major target groups: 1. Our corporate customers 2. The mainly younger crowd executing the tasks on our platform.
The target group of customers are Influencers and decision makers with companies and other organizations in with large administrative and customer service departments. Most information in the startup phase will be targeting this group.
The target group of future crowd workers will be heterogeneous, from students to stay at home mums or night shift workers who want to earn some extra money by performing easy to execute microtasks in the cloud. We will target both Dutch and international workers.

The website must be developed for browsing on a computer but also be optimized for mobile devices and tablets.
The website must be optimized and tested for the major browsers on windows, macOS and mobile devices.

For the minimum requirement for the website see attached wireframes

The present landing page http://thepinegladeloft.com and logo are not reflecting our preferences!
See enclosed a new logo that stands for both the crowdwork (performed for our customers) and the crowd (the pine glade loft).

Target Market(s)

see tekst above.

Industry/Entity Type

Business Service

Coding

Coded - Design and coding required

Number of Pages Required

5+ page

Font styles to use
Sans Serif
Other font styles liked:
• Lato, Open Sans

Colors

Designer to choose colors to be used in the design.

Requirements
Must have
• start devider screen
• home page displaying business and worker information
• a page displaying only info for businesses
• a page displaying only info for workers
• a contact form
• a reviews page
• color scheme from logo
• responsiveness!
Nice to have
• Nice animations
• overlapping blocks, animated on scroll
• lightbox effects if applicable
• animated mobile menu icon and menu itself

```html
<!DOCTYPE html>
<html lang="en">
<head>
<meta charset="utf-8">
<title>The Pine Glade Loft — Crowdsourcing</title>
<link rel="stylesheet" href="https://fonts.googleapis.com/css2?family=Montserrat:wght@400;600;700&family=Open+Sans:wght@400;600&display=swap">
<style>
:root{
  --orange:#f08a0a;
  --ink:#111;
  --text:#555;
  --paper:#fff;
  --mist:#f4f4f4;
  --footer:#8b8c8e;
}
*{margin:0;padding:0;box-sizing:border-box}
html,body{width:796px;height:1200px;overflow:hidden;background:var(--paper)}
body{position:relative;font-family:"Open Sans",Arial,sans-serif;color:var(--text)}
.abs{position:absolute}
.site-header{top:0;left:0;width:796px;height:46px;background:var(--paper)}
.brand{font-family:"Montserrat",Arial,sans-serif;font-weight:700;color:var(--orange);display:flex;align-items:center;gap:6px;line-height:1;white-space:nowrap}
.brand-dot{width:10px;height:10px;border-radius:50%;background:#7a7a7a;flex:none}
.site-header .brand{left:140px;top:15px;font-size:15px}
.nav{right:234px;top:19px;display:flex;gap:11px;font-family:"Montserrat",Arial,sans-serif;font-size:7.5px;font-weight:600;color:#222;white-space:nowrap}
.btn-solid{background:var(--orange);color:#fff;font-family:"Montserrat",Arial,sans-serif;font-weight:700;display:flex;align-items:center;justify-content:center;white-space:nowrap}
.header-cta{left:574px;top:13px;width:82px;height:21px;font-size:7.5px}
.hero{top:46px;left:0;width:796px;height:244px;background:linear-gradient(180deg,#3a3c40 0%,#2a2c30 55%,#4a4a48 100%)}
.hero-title{top:78px;width:796px;text-align:center;font-family:"Montserrat",Arial,sans-serif;font-weight:700;color:#fff;font-size:31px}
.hero-sub{top:116px;width:796px;text-align:center;font-family:"Montserrat",Arial,sans-serif;font-weight:600;color:#fff;font-size:17px}
.hero-cta{left:372px;top:158px;width:80px;height:23px;font-size:11px}
.hero-arrow{left:387px;top:201px}
.offer{top:290px;left:0;width:796px;height:172px;background:var(--mist)}
.offer-mark{left:391px;top:17px;width:14px;height:14px;border-radius:50%;background:var(--orange)}
.offer h2{top:60px;width:796px;text-align:center;font-family:"Montserrat",Arial,sans-serif;color:var(--ink);font-weight:600;font-size:19.5px;line-height:1.2}
.offer h2 span{display:block;font-size:16px}
.offer p{top:116px;left:218px;width:360px;text-align:center;font-size:8.6px;line-height:1.55}
.photo-faded{opacity:.35}
.frame{border-color:var(--orange);border-style:solid}
.feature-title{font-family:"Montserrat",Arial,sans-serif;font-weight:600;font-size:15px;line-height:1.25;color:var(--ink);width:230px}
.feature-lead{font-size:8px;line-height:1.55;font-weight:600;color:var(--orange);width:245px}
.feature-body{font-size:8px;line-height:1.55}
.btn-outline{border:1px solid var(--orange);color:var(--orange);font-family:"Montserrat",Arial,sans-serif;font-weight:700;font-size:7px;display:flex;align-items:center;justify-content:center;width:55px;height:20px}
.trending{top:1033px;left:0;width:796px;height:50px;background:var(--orange);color:#fff}
.trending-label{position:absolute;left:140px;top:18px;font-family:"Montserrat",Arial,sans-serif;font-size:10.5px}
.trending-list{position:absolute;left:237px;top:20px;width:393px;overflow:hidden;white-space:nowrap;font-size:8.5px;display:flex;gap:14px}
.site-footer{top:1083px;left:0;width:796px;height:117px;background:var(--footer);color:#fff}
.site-footer .brand{left:140px;top:30px;font-size:12px;color:#fff}
.copyright{left:140px;top:69px;font-size:6px}
.footer-links{left:305px;top:24px;font-family:"Montserrat",Arial,sans-serif;font-weight:600;font-size:8px;line-height:15.5px;list-style:none}
.footer-links li::before{content:"›";margin-right:5px}
.contact{left:513px;top:31px;font-size:7px;line-height:15px}
.contact .phone{font-size:10px;font-weight:600}
.contact svg{vertical-align:-1px;margin-right:5px}
</style>
</head>
<body>

<header class="site-header abs">
  <div class="brand abs"><span class="brand-dot"></span>The Pine Glade Loft</div>
  <nav class="nav abs"><span>HOME</span><span>FOR BUSINESSES</span><span>FOR WORKERS</span></nav>
  <div class="btn-solid header-cta abs">GET IN CONTACT</div>
</header>

<section class="hero abs" role="img" aria-label="Photo of a large open-plan office full of people working at computers">
  <h1 class="hero-title abs">Crowdsourcing to improve</h1>
  <div class="hero-sub abs">your customers satisfaction &amp; reduce costs</div>
  <div class="btn-solid hero-cta abs">CONTACT US</div>
  <svg class="hero-arrow abs" width="22" height="12" viewBox="0 0 22 12"><polyline points="1,1 11,11 21,1" fill="none" stroke="#fff" stroke-width="1.5"/></svg>
</section>

<section class="offer abs">
  <div class="offer-mark abs"></div>
  <h2 class="abs">We offer specialised crowd workers for your<span>bulk business processes</span></h2>
  <p class="abs">You are a mid to large-sized entreprise and you need to be increasingly scalable due to the fast changing markets. You want to have an unlimited workforce (the crowd) but you don't want all the hassle of employees.</p>
</section>

<div class="abs photo-faded" style="left:0;top:496px;width:343px;height:199px;background:linear-gradient(90deg,#c9ccd2,#e8eaee)" role="img" aria-label="Faded office meeting photo"></div>
<div class="abs frame" style="left:200px;top:560px;width:178px;height:158px;border-width:0 2px 2px 0"></div>
<div class="abs" style="left:155px;top:521px;width:220px;height:193px;background:linear-gradient(135deg,#d8dde3,#8e99a6 60%,#cfd4d9)" role="img" aria-label="Photo of two businessmen reviewing documents at an office desk"></div>
<h3 class="feature-title abs" style="left:402px;top:507px">Praesent viverra nunc sit amet orci suscipit maximus</h3>
<p class="feature-lead abs" style="left:402px;top:555px">Maecenas at risus justo. Mauris vel odio aliquam, vehicula ante sed, laoreet magna. Aliquam quis tempor sem.</p>
<p class="feature-body abs" style="left:402px;top:592px;width:254px">Aliquam quis erat id velit dignissim bibendum. Ut cursus nisi nec leo auctor, rhoncus laoreet massa finibus. Donec euismod nec elit a condimentum. Quisque sit amet nunc non nisl sollicitudin euismod. Maecenas aliquet sapien felis, ut mollis odio fringilla et. Aliquam consequat nunc id dui laoreet tincidunt.Maecenas at risus justo. Mauris vel odio aliquam, vehicula ante sed, laoreet magna. Aliquam quis tempor sem. Aliquam quis erat id velit dignissim bibendum.</p>
<div class="btn-outline abs" style="left:599px;top:694px">READ MORE</div>

<div class="abs photo-faded" style="left:445px;top:767px;width:351px;height:199px;background:linear-gradient(90deg,#e8b88a,#f2e0cf)" role="img" aria-label="Faded photo of people working in a booth"></div>
<div class="abs frame" style="left:406px;top:830px;width:60px;height:158px;border-width:0 0 2px 2px"></div>
<div class="abs" style="left:411px;top:791px;width:219px;height:194px;background:linear-gradient(135deg,#c8651f,#a24a14 55%,#e9e4de)" role="img" aria-label="Photo of two young people working on laptops in an orange booth"></div>
<h3 class="feature-title abs" style="left:140px;top:776px">Praesent viverra nunc sit amet orci suscipit maximus</h3>
<p class="feature-lead abs" style="left:140px;top:825px">Maecenas at risus justo. Mauris vel odio aliquam, vehicula ante sed, laoreet magna. Aliquam quis tempor sem.</p>
<p class="feature-body abs" style="left:140px;top:861px;width:245px">Aliquam quis erat id velit dignissim bibendum. Ut cursus nisi nec leo auctor, rhoncus laoreet massa finibus. Donec euismod nec elit a condimentum. Quisque sit amet nunc non nisl sollicitudin euismod. Maecenas aliquet sapien felis, ut mollis odio fringilla et. Aliquam consequat nunc id dui laoreet tincidunt.Maecenas at risus justo. Mauris vel odio aliquam, vehicula ante sed, laoreet magna. Aliquam quis tempor sem. Aliquam quis erat id velit dignissim bibendum.</p>
<div class="btn-outline abs" style="left:140px;top:963px">READ MORE</div>

<div class="trending abs">
  <span class="trending-label">Trending Topics :</span>
  <div class="trending-list"><span>laoreet magna,</span><span>Aliquam quis tempor sem,</span><span>Aliquam quis erat,</span><span>id velit dignissim bibendum,</span><span>Aliquam quis erat</span></div>
</div>

<footer class="site-footer abs">
  <div class="brand abs"><span class="brand-dot" style="background:#fff"></span>The Pine Glade Loft</div>
  <div class="copyright abs">Copyright 2017 - All rights reserved</div>
  <ul class="footer-links abs"><li>HOME</li><li>FOR BUSINESSES</li><li>FOR WORKERS</li></ul>
  <div class="contact abs">
    <div><svg width="8" height="6" viewBox="0 0 8 6"><rect width="8" height="6" fill="#fff"/><polyline points="0,0 4,3.5 8,0" fill="none" stroke="#8b8c8e" stroke-width="0.8"/></svg>INFO@THEPINEGLADELOFT.COM</div>
    <div class="phone"><svg width="7" height="8" viewBox="0 0 7 8"><path d="M1 0h2l.5 2-1 1c.5 1 1 1.6 2 2l1-1 1.5.6V7c0 .6-.5 1-1 1C2.5 8 0 5 0 1c0-.5.4-1 1-1z" fill="#fff"/></svg>-0698 745 210</div>
  </div>
</footer>

</body>
</html>
```